Newsletter/Flyer/Advertisement - ("Call for Papers") Design Project

We will be arranging a conference on electronics integration technology in Helsinki, Finland in September 2014 and we would need catchy looking information leaflet to advertise it. We call this a “call for papers” and it is distributed to all potential attendants of the conference. I have attached the plain text part as a MS Word document “1st Call for Papers.docx”. The title format, font etc. can be changed and modified but the 1/2/1 column layout should remain the same and the text should not extend to third page.
There are 5 logos that must be included; the event logo KVRD2014 should be on the front page but the remaining 4 logos (Brenmoor University, OQJU, LDSW, and uNOLT) should be placed in the bottom footer of both pages. I have attached the call for papers from the previous KVRD conference (in 2012) as a reference of how it has looked before. However, I would like to make it visually little bit more like the GYPB call for papers, which is also attached. If you can find a little "flavor" perhaps from the theme of the conference (electronics) and/or something local (Helsinki) to make it stand out next to the old KVRD one. I think the theme of electronics is quite universal but I will also attach some photos of Helsinki.
Please do not hesitate to ask for clarifications!
Updates

Target Market(s)

Technical people and academics around the world

Industry/Entity Type

Electronics

Requirements
Must have
• Texh included in the "1st Call for Papers.docx". 5 logos: the KVRD2014 event logo somewhere up in the front; Brenmoor University, OQJU, LDSW, and uNOLT logos down in the bottom footer (in this particular order).
Nice to have
• Some local "flavor" from Helsinki and the theme of the conference (microelectronics) present in the appearance.

```html
<!DOCTYPE html>
<html lang="en">
<head>
<meta charset="utf-8">
<title>KVRD 2014 – First Call for Paper</title>
<link rel="stylesheet" href="https://fonts.googleapis.com/css2?family=Arimo:ital,wght@0,400;0,700;1,400;1,700&family=Open+Sans+Condensed:wght@700&family=Rambla:wght@700&family=Noto+Serif:ital,wght@1,700&display=swap">
<style>
  :root {
    --navy: #0f1c33;
    --navy-deep: #0a1426;
    --sky: #3b8fdc;
    --bar: #8fa9cf;
    --bar-dark: #6f8fbe;
    --body-bg: #e3e9f2;
    --ink: #16243a;
    --link: #1d4fb0;
    --green: #4f6a2a;
    --grey: #555d66;
    --white: #ffffff;
  }
  * { box-sizing: border-box; margin: 0; padding: 0; }
  html, body { width: 831px; height: 1200px; overflow: hidden; background: var(--white); }
  body { font-family: "Arimo", Arial, sans-serif; color: var(--ink); }
  .flyer { position: relative; width: 831px; height: 1200px; overflow: hidden; background: var(--body-bg); }

  .city-photo { position: absolute; left: 0; top: 0; width: 831px; height: 145px;
    background: linear-gradient(180deg, #0b1a33 0%, #1d3457 45%, #4a5663 70%, #1a2738 100%); }
  .title-band { position: absolute; left: 0; top: 145px; width: 831px; height: 87px; background: var(--navy); }
  .circuit-field { position: absolute; left: 0; top: 232px; width: 831px; height: 870px;
    background: radial-gradient(ellipse at 50% 50%, #f2f5fa 0%, #dfe6f0 55%, #c9d4e4 100%); }

  .event-mark { position: absolute; right: 18px; top: 22px; width: 270px; height: 100px;
    display: flex; align-items: center; justify-content: center; gap: 12px; }
  .event-mark .square { width: 26px; height: 26px; background: var(--sky); }
  .event-mark .name { font-weight: 700; font-size: 44px; color: var(--white); letter-spacing: 1px; }

  .headline { position: absolute; left: 18px; top: 148px; font-family: "Open Sans Condensed", "Arial Narrow", sans-serif;
    font-weight: 700; font-size: 50px; color: var(--white); letter-spacing: 0.5px; line-height: 1; }
  .dateline { position: absolute; left: 22px; top: 207px; font-family: "Noto Serif", Georgia, serif;
    font-style: italic; font-weight: 700; font-size: 14px; color: #c6d2e6; }
  .conf-name { position: absolute; left: 520px; top: 158px; width: 311px; text-align: center;
    font-weight: 700; font-size: 19px; line-height: 1.35; color: var(--sky); }

  .column { position: absolute; top: 276px; font-size: 13.6px; line-height: 1.55; text-align: justify; }
  .column.left { left: 35px; width: 345px; }
  .column.right { left: 449px; width: 348px; top: 278px; }
  .column p { margin-bottom: 21px; }
  .topic-label { color: var(--link); font-weight: 700; }
  .section-bar { background: linear-gradient(90deg, var(--bar-dark), var(--bar)); color: var(--navy);
    font-weight: 700; font-size: 18px; line-height: 1.3; padding: 4px 10px; margin-bottom: 4px; }
  .column.left .section-bar { color: var(--white); margin-top: 0; margin-bottom: 5px; }
  .column.right p { margin-bottom: 0; }
  .block { margin-bottom: 20px; }
  .web { color: var(--link); text-decoration: underline; }
  .key-dates { list-style: none; }
  .key-dates li::before { content: "• "; }

  .closing { position: absolute; left: 0; top: 958px; width: 831px; text-align: center;
    font-family: "Rambla", "Arimo", sans-serif; font-weight: 700; font-size: 20.5px; line-height: 1.3; color: var(--green); }
  .signatures { position: absolute; top: 1041px; left: 0; width: 831px; font-size: 14px; color: var(--grey); }
  .signer { position: absolute; }
  .signer em { display: block; }
  .signer.general { left: 95px; }
  .signer.executive { left: 409px; }
  .signer.program { left: 650px; text-align: right; }

  .partner-strip { position: absolute; left: 0; top: 1102px; width: 831px; height: 72px; background: var(--white);
    display: flex; align-items: center; padding-left: 190px; gap: 34px; }
  .partner { display: flex; align-items: center; gap: 6px; font-weight: 700; font-size: 15px; color: var(--navy); }
  .partner .dot { width: 14px; height: 14px; background: var(--navy); }
  .partner .dot.round { border-radius: 50%; }
  .board-photo { position: absolute; right: 8px; top: 1104px; width: 88px; height: 68px;
    background: linear-gradient(135deg, #2f5fb0, #1b3c7c); }
  .footer-bar { position: absolute; left: 0; top: 1174px; width: 831px; height: 26px; background: var(--navy-deep);
    color: var(--white); font-size: 11px; font-weight: 700; text-align: center; line-height: 26px; }
</style>
</head>
<body>
<main class="flyer">
  <div class="city-photo" role="img" aria-label="Night view of the Helsinki waterfront with the lit cathedral dome"></div>
  <div class="title-band"></div>
  <div class="circuit-field" role="img" aria-label="Faint printed circuit board traces in pale blue"></div>

  <div class="event-mark"><span class="square"></span><span class="name">KVRD2014</span></div>

  <h1 class="headline">First Call for Paper</h1>
  <p class="dateline">September 15 – 18, 2014, Helsinki, Finland</p>
  <p class="conf-name">Circuit Module-assembly<br>Research Conference</p>

  <section class="column left">
    <p><span class="topic-label">Printable electronics:</span> printed/jetted (transparent) conductors, touch sensors, screens and displays (e.g. OLED), paper electronics, 3D printing, PV, etc.</p>
    <p><span class="topic-label">Reliability:</span> challenges at different levels of investigations (system, board, package and joint), characterization and test methods, interconnection reliability; characterization, and next generation/novel packaging reliability.</p>

    <h2 class="section-bar">Abstract Submission</h2>
    <p>You are invited to submit a 300-500 word abstract that describes the scope, content and key points of your proposed paper. Abstracts must include results and graphics. The official language of all presentations is English. Please visit <span class="web">www.kvrd2014.eu</span> to find more information and to upload your abstract. Submission of abstracts will be opened 1.1.2014 and the abstracts are <strong>due 28.2.2014</strong>. All abstracts must be submitted electronically at the conference web site.</p>
    <p>All submitted abstracts will be reviewed by the committee to ensure a high-quality conference. Authors will be notified of paper acceptance with instructions for publication by 18.4.2014.</p>
    <p>If you have any questions, please contact: Henrik Valdane, Program Chair of the 5<sup style="font-size:8px;line-height:0">th</sup> KVRD, via email (firstname.lastname@nordvel.fr).</p>
  </section>

  <section class="column right">
    <div class="block">
      <h2 class="section-bar">Publication of Papers</h2>
      <p>All oral and poster presentation papers will be included in the conference proceedings and made available at the OQJU Vaultline Digital Library (<em>vaultline.oqju.org</em>).<br>In order to be included in OQJU Vaultline the paper must be original and not previously published, and avoid inclusion of commercial content.</p>
    </div>
    <div class="block">
      <h2 class="section-bar">Best Paper Awards</h2>
      <p>KVRD will select the best paper presentation. The author(s) will receive a personalized KVRD award and share a check for EUR 1 000.<br>KVRD will select the best poster whose author(s) will receive a personalized KVRD award and share a check for EUR 1 000.</p>
    </div>
    <div class="block">
      <h2 class="section-bar">Professional Development Courses</h2>
      <p style="text-align:left">In addition to abstracts for papers we call proposals from individuals interested in teaching educational professional development courses (4 hours) on the topics described in the Call for Papers. Proposal should be submitted to Henrik Valdane, the Program Chair of the 5th KVRD, via email (<span class="web">firstname.lastname@nordvel.fr</span>) also by <strong>28.2.2014</strong>.</p>
    </div>
    <div class="block">
      <h2 class="section-bar">Professional Development Courses</h2>
      <ul class="key-dates">
        <li>Abstract submission: <strong>28.2.2014</strong></li>
        <li>Notification of acceptance: <strong>18.4.2014</strong></li>
        <li>Papers in the final form: <strong>20.6.2014</strong></li>
      </ul>
    </div>
  </section>

  <p class="closing">We look forward to welcoming you to the fourth OQJU-LDSW Circuit Module-<br>assembly Research Conference KVRD 2014 in Helsinki!</p>

  <div class="signatures">
    <div class="signer general">Liisa Marjoranta-Holm<em>General Chair</em></div>
    <div class="signer executive">Eero Kalsta<em>Executive Chair</em></div>
    <div class="signer program">Henrik Valdane<em>Program Chair</em></div>
  </div>

  <div class="partner-strip">
    <span class="partner"><span class="dot"></span>Brenmoor University</span>
    <span class="partner"><span class="dot"></span>OQJU</span>
    <span class="partner"><span class="dot round"></span>LDSW</span>
    <span class="partner"><span class="dot round"></span>uNOLT</span>
  </div>
  <div class="board-photo" role="img" aria-label="Blue electronic circuit board module"></div>

  <footer class="footer-bar">www.kvrd2014.eu (http://10.48.216.37)</footer>
</main>
</body>
</html>
```